Clean and Polished Store Design

Please design a website similar to this one: http://veltrasign.com/
We require two pages:
* the home page: http://veltrasign.com/
* the product page: http://veltrasign.com/products/our-printer
Notice that there are few words and more pictures. It's clean and professional. Although I think their product page is difficult to read because it is too spread out.
Please help us generate excitement for our product via a polished and high-end looking web design. Please keep it VERY SIMPLE.
Target Market(s)
Our target market is consumers that have never bought a 3D printer before and those to whom 3D printing is new but exciting. Our market is not very technical. They love the sleek look of the printer and its ease of use.
Industry/Entity Type
Printer
Requirements
Must have
- We require two pages:
- * the home page: http://veltrasign.com/
- * the product page: http://veltrasign.com/products/our-printer
- One of our product renderings must be displayed on both the homepage and the product page.
- Our logo must be displayed on both pages.
- The pages must have a header, a footer and content equivalent to the veltrasign website.

```html
<!DOCTYPE html>
<html lang="en">
<head>
<meta charset="utf-8">
<title>Veltrasign — High Resolution Desktop 3D Printer</title>
<link href="https://fonts.googleapis.com/css2?family=Montserrat:wght@400;600;700&family=PT+Sans:wght@400;700&display=swap" rel="stylesheet">
<style>
:root{
  --ink:#1c1c1c;
  --teal:#5aaab9;
  --teal-deep:#1a9dbd;
  --link:#0e95b4;
  --nav-top:#6e6e6e;
  --nav-bot:#4b4b4b;
  --page:#ececec;
  --card:#ffffff;
  --text:#444444;
  --muted:#8a8a8a;
  --rule:#c9c9c9;
  --foot-top:#5a5a5a;
  --foot-bot:#7a7a7a;
}
*{box-sizing:border-box;margin:0;padding:0}
html,body{width:1200px;height:1057px;overflow:hidden}
body{position:relative;background:var(--page);font-family:"PT Sans",sans-serif;color:var(--text)}
.abs{position:absolute}

/* brand name: plain text with a single circle */
.brand{display:flex;align-items:center;gap:8px;font-family:"PT Sans",sans-serif;font-weight:700;color:var(--ink);white-space:nowrap}
.brand-dot{display:inline-block;border-radius:50%;background:var(--teal)}

/* header */
.site-header{left:0;top:0;width:1200px;height:79px;background:#fff}
.site-header .brand{left:190px;top:16px;font-size:40px;line-height:44px}
.site-header .brand-dot{width:18px;height:18px}
.top-actions{left:723px;top:27px;display:flex;gap:3px}
.top-btn{height:28px;background:var(--teal);color:#fff;font-family:"Montserrat",sans-serif;font-weight:600;font-size:12px;letter-spacing:1.5px;display:flex;align-items:center;justify-content:center;border-radius:2px}
.top-btn svg{margin-right:6px}

/* nav */
.main-nav{left:0;top:79px;width:1200px;height:31px;background:linear-gradient(var(--nav-top),var(--nav-bot));border-top:1px solid #888;border-bottom:1px solid #3c3c3c}
.main-nav ul{list-style:none;display:flex;position:absolute;left:181px;top:0;height:30px;border-left:1px solid #3f3f3f}
.main-nav li{height:30px;display:flex;align-items:center;justify-content:center;color:#f2f2f2;font-family:"Montserrat",sans-serif;font-weight:600;font-size:11px;letter-spacing:2px;border-right:1px solid #3f3f3f;box-shadow:inset 1px 0 0 #7a7a7a;white-space:nowrap}

/* hero */
.hero{left:0;top:110px;width:1200px;height:270px;background:radial-gradient(ellipse at 62% 45%,#f7f7f7 0%,#c8c8c8 45%,#9a9a9a 100%)}
.hero-copy{left:248px;top:22px;width:400px;text-align:center;color:#fff;font-family:"Montserrat",sans-serif;font-weight:700;text-shadow:0 1px 2px rgba(0,0,0,.45)}
.hero-copy h1{font-size:22px;line-height:33px;letter-spacing:2.4px}
.hero-copy h2{margin-top:12px;font-size:24px;line-height:34px;letter-spacing:2.4px;font-weight:600}
.order-btn{left:365px;top:214px;width:159px;height:36px;background:linear-gradient(#7c7c7c,#555);border-radius:2px;color:#eee;font-family:"Montserrat",sans-serif;font-weight:700;font-size:14px;letter-spacing:2px;display:flex;align-items:center;justify-content:center;gap:12px;box-shadow:0 1px 2px rgba(0,0,0,.4)}
.hero-render{left:722px;top:14px;width:258px;height:250px;border-radius:28px;background:linear-gradient(135deg,#ffffff,#e4e4e4 60%,#c6c6c6)}
.zigzag{left:0;top:380px;width:1200px;height:8px}

/* content */
.content-card{left:180px;top:380px;width:840px;height:446px;background:var(--card)}
.video{left:191px;top:402px;width:393px;height:217px;background:linear-gradient(135deg,#8d7a62,#b6a58c 45%,#5c544b)}
.video-badge{left:199px;top:409px;width:131px;height:52px;background:#fff;display:flex;align-items:center;justify-content:center}
.video-badge .brand{font-size:20px;gap:5px}
.video-badge .brand-dot{width:9px;height:9px}
.video-title{left:333px;top:413px;height:20px;padding:0 4px;background:rgba(40,40,40,.75);color:var(--teal);font-family:Arial,sans-serif;font-weight:700;font-size:15px;line-height:20px;white-space:nowrap}
.video-bar{left:199px;top:577px;width:377px;height:34px;background:rgba(25,25,25,.82);border-radius:3px}
.video-time{left:255px;top:577px;background:#fff;color:#222;font-size:10px;padding:0 3px;line-height:12px}
.video-track{left:270px;top:590px;width:150px;height:10px;border:1px solid #888}
.video-host{left:512px;top:585px;color:#fff;font-weight:700;font-size:14px}

.welcome-bar{left:584px;top:418px;width:425px;height:28px;background:#e8e8e8;text-align:center;font-family:"Montserrat",sans-serif;font-weight:600;font-size:19px;letter-spacing:1.5px;line-height:28px;color:#333}
.welcome-bar span{color:var(--link)}
.welcome-sub{left:600px;top:462px;width:400px;text-align:center;color:var(--link);font-weight:700;font-size:14.5px;line-height:21.5px;letter-spacing:.6px}
.welcome-body{left:630px;top:517px;width:340px;text-align:center;font-size:14.5px;line-height:21.5px;letter-spacing:.4px}
.welcome-body a{color:var(--link);font-weight:700;text-decoration:underline}

.press-grid{left:188px;top:638px;width:823px;height:171px;display:grid;grid-template-columns:164px 171px 164px 164px 160px;grid-template-rows:1fr 1fr;border-top:1px dotted var(--rule);border-bottom:1px dotted var(--rule)}
.press-grid div{display:flex;align-items:center;justify-content:center;border-right:1px dotted var(--rule);color:var(--muted);font-size:19px;font-weight:700;letter-spacing:.5px;white-space:nowrap}
.press-grid div:nth-child(5n){border-right:0}
.press-grid div:nth-child(-n+5){border-bottom:1px dotted var(--rule)}
.press-grid div:nth-child(5n+1){border-left:1px dotted var(--rule)}

/* signup */
.signup{left:0;top:826px;width:1200px;height:80px;background:linear-gradient(#fdfdfd,#e4e4e4)}
.signup-label{left:192px;top:856px;font-size:19px;letter-spacing:1.2px;color:#555}
.signup-input{left:484px;top:853px;width:305px;height:32px;border:1px solid #ccc;border-bottom:2px solid #bbb;border-radius:2px;background:linear-gradient(#fff,#f2f2f2);color:#999;font-size:14px;letter-spacing:.6px;padding:7px 11px}
.signup-btn{left:802px;top:853px;width:150px;height:32px;background:var(--teal-deep);border-bottom:2px solid #0f7c96;border-radius:2px;color:#fff;font-weight:700;font-size:16px;display:flex;align-items:center;justify-content:center}

/* footer */
.site-footer{left:0;top:906px;width:1200px;height:151px;background:linear-gradient(var(--foot-top),var(--foot-bot))}
.footer-links{left:199px;top:927px;display:flex;color:#fff;font-family:"Montserrat",sans-serif;font-size:12.5px;letter-spacing:1.6px}
.footer-links span.sep{margin:0 15px;color:#ddd}
.footer-legal{left:199px;top:963px;color:#fff;font-family:"Montserrat",sans-serif;font-size:11.5px;letter-spacing:1px}
.site-footer .brand{position:absolute;left:201px;top:100px;font-size:24px;gap:6px}
.site-footer .brand-dot{width:10px;height:10px}
.social{left:370px;top:1002px;display:flex;gap:2px}
.social i{display:block;width:29px;height:34px;border-radius:3px;background:#9a9a9a}
.footer-render{background:linear-gradient(135deg,#fff,#dcdcdc 60%,#bdbdbd);border-radius:12px}
</style>
</head>
<body>

<header class="site-header abs">
  <div class="brand abs"><span>Veltrasign</span><span class="brand-dot"></span></div>
  <nav class="top-actions abs">
    <a class="top-btn" style="width:80px">STORE</a>
    <a class="top-btn" style="width:80px">LOGIN</a>
    <a class="top-btn" style="width:129px"><svg width="16" height="13" viewBox="0 0 16 13"><path d="M0 1h3l2 8h9l2-6H4" fill="none" stroke="#fff" stroke-width="1.6"/><circle cx="6" cy="11.5" r="1.3" fill="#fff"/><circle cx="12" cy="11.5" r="1.3" fill="#fff"/></svg>CART (0.00)</a>
  </nav>
</header>

<nav class="main-nav abs">
  <ul>
    <li style="width:85px">HOME</li>
    <li style="width:125px">THE VELA ONE</li>
    <li style="width:78px">BLOG</li>
    <li style="width:103px">SUPPORT</li>
    <li style="width:113px">ABOUT US</li>
  </ul>
</nav>

<section class="hero abs">
  <div class="hero-copy abs">
    <h1>THE PRECISION OF<br>STEREOLITHOGRAPHY.<br>RIGHT ON YOUR DESKTOP.</h1>
    <h2>High Resolution<br>Desktop 3D Printer</h2>
  </div>
  <a class="order-btn abs">ORDER NOW <svg width="11" height="12" viewBox="0 0 11 12"><path d="M0 0l11 6-11 6z" fill="#eee"/></svg></a>
  <div class="hero-render abs" role="img" aria-label="Product rendering of the white cube-shaped Vela One desktop 3D printer"></div>
</section>
<svg class="zigzag abs" viewBox="0 0 1200 8" preserveAspectRatio="none"><pattern id="zz" width="6" height="8" patternUnits="userSpaceOnUse"><path d="M0 2L3 6 6 2" fill="none" stroke="#bdbdbd" stroke-width="1"/></pattern><rect width="1200" height="8" fill="url(#zz)"/></svg>

<main>
  <div class="content-card abs"></div>

  <div class="video abs" role="img" aria-label="Video still: the Vela One printer on a desk beside a monitor showing a 3D model"></div>
  <div class="video-badge abs"><div class="brand"><span>Veltrasign</span><span class="brand-dot"></span></div></div>
  <div class="video-title abs">Introducing the Vela One</div>
  <div class="video-bar abs"><svg style="position:absolute;left:20px;top:9px" width="14" height="16" viewBox="0 0 14 16"><path d="M0 0l14 8-14 8z" fill="#fff"/></svg></div>
  <div class="video-time abs">03:28</div>
  <div class="video-track abs"></div>
  <div class="video-host abs">Clipwave</div>

  <h3 class="welcome-bar abs">Welcome <span>To Veltrasign</span></h3>
  <p class="welcome-sub abs">The Precision of Stereolithography.<br>Right on Your Desktop.</p>
  <p class="welcome-body abs">The Vela One marries high-end stereolithography (SL) technology and a seamless user experience at a price affordable to the professional designer, engineer and maker. <a>Learn more</a></p>

  <div class="press-grid abs">
    <div>Cableline</div><div>TechGrind</div><div>gadgetry</div><div>Hopwire</div><div>form88</div>
    <div>Tradeonomy</div><div>Build:</div><div>The Brink</div><div>Harbor Ledger</div><div>Swift Venture</div>
  </div>
</main>

<section class="signup abs"></section>
<div class="signup-label abs">Get Updates on Our Progress:</div>
<div class="signup-input abs">Email Address :</div>
<a class="signup-btn abs">Stay in touch</a>

<footer class="site-footer abs">
  <div class="brand"><span>Veltrasign</span><span class="brand-dot"></span></div>
  <div class="footer-render abs" style="left:725px;top:78px;width:63px;height:62px" role="img" aria-label="Small Vela One printer rendering"></div>
  <div class="footer-render abs" style="left:806px;top:48px;width:80px;height:77px" role="img" aria-label="Medium Vela One printer rendering"></div>
  <div class="footer-render abs" style="left:904px;top:20px;width:100px;height:98px" role="img" aria-label="Large Vela One printer rendering"></div>
</footer>
<div class="footer-links abs"><span>HOME</span><span class="sep">I</span><span>BLOG</span><span class="sep">I</span><span>SUPPORT</span><span class="sep">I</span><span>ABOUT US</span><span class="sep">I</span><span>STORE</span><span class="sep">I</span><span>CAREERS</span></div>
<div class="footer-legal abs">© veltrasign 2013 - Privacy Policy - Terms of Service</div>
<div class="social abs"><i></i><i></i><i></i><i></i></div>

</body>
</html>
```